Law Enforcement Consulting Group Website

We are working with a Law Enforcement Consulting Group called Brennock Group. They help law enforcement agencies develop policies, training tools, solve problems, etc...

Some sites to use for content/competitors:
https://harrowfieldpartners.com
https://veltranorix.com/military-law/law-enforcement-consulting-services/
https://harrowfieldpartners.com/services/police-services/

Consulting websites for inspiration ( we found these sites to fit better with the brand, and identity of the client:

https://drum.quelby
https://tidalvoxen.co
https://www.torvendabrill.com
https://quellaromberti.com
https://perisovandeh.com
https://themes.pebblecrate.com/be/consultant2/
https://themes.pebblecrate.com/be/consultant/

Thank you for taking the time to consider designing a website for us. We are web developers based in Stockton, CA, USA. Most of our projects go through the same process. Understanding this process may help you win a project with us. We custom-code all of our websites in-house. We don’t have any requirements as to what tools you use for your design, but we prefer Figma files. For any design that we label as four-stars, we send it to the client for review. The client picks the final design they want us to use. Once we complete this process, we will continue to show additional clients all the four-star sites and purchase them later. Your designs will have multiple chances to sell. For better chances of success, we ask that you follow these guidelines.

IMAGES:
If you use any images or icons in the design, we ask that you have a link to the asset so we can purchase the image/icon. Most of the designs we submit do not have the customer’s images on them unless they have some great images. Be creative; show us the feeling you are trying to portray with your image choices. Use any royalty-free site you choose. We subscribe to Adobe and mainly use their images, but we can purchase images outside of Adobe.
PLEASE NOTE: we will not submit designs to clients with watermarks on the images.

FONTS:
We ask that you identify the fonts used in the design. This can be done in a message if you want. We typically use Google Fonts and Adobe Fonts.

CONTENT:
We're always open to different content and ideas. We often submit designs with stock images so the client can see our vision. We typically take pictures after the website launch to use their images with our vision. Lorem Ipsum is fine for paragraphs, but we ask that you write the headers in correct English. We want to be able to show the vision and identify the sections of the website.

INSPIRATION:
We typically add a couple of links in the brief of websites we like to help you get started in your design.

REVISIONS:
We do not often ask for revisions of the designs unless we see something in the design that may not appeal to the client. If there are slight changes that we want to make, we do that in the development process.

FEEDBACK:
We rarely give feedback on designs during the design process. We are working on many website projects and do not have the time to provide feedback. We usually respond if your request is well thought out and asks specific questions, but a note asking “feedback, please” usually goes unanswered.

```html
<!DOCTYPE html>
<html lang="en">
<head>
<meta charset="utf-8">
<title>Brennock Group — Law Enforcement Security Consulting</title>
<link rel="stylesheet" href="https://fonts.googleapis.com/css2?family=Lexend:wght@300;400;600;800&family=Arimo:wght@400;700&display=swap">
<style>
:root{
  --orange:#e2471c;
  --orange-dark:#b8360f;
  --ink:#1f1b19;
  --brown:#3a1c12;
  --text:#555;
  --light:#f7f0ec;
  --slate:#6e7380;
  --white:#fff;
}
*{box-sizing:border-box;margin:0;padding:0}
html,body{width:1200px;height:5391px;overflow:hidden;background:#fff}
body{font-family:"Arimo",Arial,sans-serif;color:var(--text)}
.page{position:relative;width:1200px;height:5391px;overflow:hidden}
.abs{position:absolute}
svg.layer{position:absolute;left:0;top:0}
.heading{font-family:"Lexend",Arial,sans-serif;text-transform:uppercase;color:var(--ink);font-size:36px;font-weight:400;letter-spacing:.5px;line-height:1.2}
.heading b{font-weight:800}
.heading.center{width:1200px;left:0;text-align:center}
.rule{position:absolute;width:44px;height:3px;background:var(--orange)}
.para{font-size:13.5px;line-height:27px;text-align:justify;color:#6a6a6a}
.btn{position:absolute;display:flex;align-items:center;justify-content:center;font-family:"Arimo",Arial,sans-serif;font-weight:700;font-size:15px;color:#fff;text-transform:uppercase;background:var(--orange);clip-path:polygon(8% 0,100% 0,92% 100%,0 100%);letter-spacing:.3px}
.btn::after{content:"";position:absolute;inset:0;border-left:4px solid var(--orange-dark)}
/* header */
.brand{display:flex;align-items:center;gap:14px}
.brand .mark{width:62px;height:62px;border:4px solid var(--orange);background:#fff}
.brand .name{font-family:"Lexend",Arial,sans-serif;font-weight:600;font-size:30px;color:var(--orange);letter-spacing:1px;text-transform:uppercase}
.call{font-family:"Arimo",Arial,sans-serif;font-weight:700;font-size:16px;color:var(--ink);display:flex;align-items:center;gap:6px}
.nav{display:flex;gap:0;font-weight:700;font-size:12.5px;color:var(--ink);text-transform:uppercase}
.nav a{color:inherit;text-decoration:none}
.nav .active{color:var(--orange);border-bottom:2px solid var(--orange)}
/* hero */
.hero-title{font-family:"Lexend",Arial,sans-serif;font-weight:300;font-size:45px;color:#fff;line-height:63px;text-transform:uppercase;letter-spacing:.5px}
.hero-sub{font-family:"Arimo",Arial,sans-serif;font-weight:700;font-size:20px;color:#fff}
.dots{position:absolute;display:flex;gap:12px}
.dots i{width:8px;height:8px;border-radius:50%;background:#fff;display:block}
.dots i.on{background:var(--orange)}
.dots.dark i{background:#fff}
/* services */
.card{position:absolute;width:296px;height:336px;text-align:center}
.card svg{position:absolute;left:0;top:0}
.card .icon{position:absolute;left:128px;top:38px;width:40px;height:46px;border:3px solid var(--orange);border-radius:6px}
.card h3{position:absolute;left:0;right:0;top:120px;font-family:"Arimo",Arial,sans-serif;font-weight:400;font-size:19px;color:var(--ink)}
.card p{position:absolute;left:36px;right:36px;top:160px;font-size:13px;line-height:23.5px;color:#666}
.card .go{position:absolute;left:137px;top:262px;width:22px;height:22px}
.card.featured h3,.card.featured p{color:#fff}
.card.featured .icon{border-color:#fff}
/* team */
.member{position:absolute;width:260px;text-align:center}
.member .photo{width:210px;height:242px;margin:0 auto;clip-path:polygon(50% 0,100% 25%,100% 75%,50% 100%,0 75%,0 25%)}
.member .name{font-family:"Arimo",Arial,sans-serif;font-weight:700;font-size:20px;color:#fff;margin-top:26px;text-transform:uppercase}
.member .role{font-size:14px;color:#e6e6e6;margin-top:6px;text-transform:uppercase}
/* why */
.reason h4{font-family:"Arimo",Arial,sans-serif;font-weight:700;font-size:18.5px;color:var(--ink)}
.reason p{font-size:13px;line-height:23.5px;color:#666;margin-top:14px;text-align:justify}
.reason svg{position:absolute;right:0;top:0}
/* contact */
.field{position:absolute;background:#fff;font-size:12.5px;color:#444;padding:12px 15px}
/* footer */
.foot-nav{display:flex;gap:0;font-weight:700;font-size:15px;color:var(--ink);text-transform:uppercase}
.copy{font-size:12.5px;color:var(--ink)}
.social{display:flex;gap:10px}
.social i{display:block;width:34px;height:34px;border-radius:50%;border:2.5px solid var(--ink)}
</style>
</head>
<body>
<div class="page">

  <!-- Header -->
  <header>
    <div class="abs brand" style="left:145px;top:18px">
      <span class="mark"></span>
      <span class="name">Brennock Group</span>
    </div>
    <div class="abs call" style="left:670px;top:18px">
      <svg width="22" height="22" viewBox="0 0 24 24"><circle cx="12" cy="12" r="12" fill="var(--orange)"/><path d="M8.5 6.5l2 2-1.2 1.6a8 8 0 0 0 4.6 4.6l1.6-1.2 2 2-1.6 2A10 10 0 0 1 6.5 8.1z" fill="#fff"/></svg>
      CALL US : +1 555 014 2278
    </div>
    <nav class="abs nav" style="left:510px;top:64px">
      <a class="active" style="width:72px">Home</a>
      <a style="width:96px">Services</a>
      <a style="width:97px">About Us</a>
      <a style="width:87px">Clients</a>
      <a>Contact</a>
    </nav>
    <div class="btn" style="left:950px;top:57px;width:104px;height:31px;font-size:13px">Login</div>
  </header>

  <!-- Hero -->
  <section>
    <svg class="layer" width="1200" height="760" viewBox="0 0 1200 760">
      <defs>
        <linearGradient id="heroGrad" x1="0" y1="0" x2="1" y2="1">
          <stop offset="0" stop-color="#6d5a4e"/>
          <stop offset=".45" stop-color="#2b2f3a"/>
          <stop offset="1" stop-color="#15181f"/>
        </linearGradient>
      </defs>
      <polygon role="img" aria-label="Consultant in a suit using a tablet in front of city office towers" points="0,105 1200,105 1200,572 600,700 0,572" fill="url(#heroGrad)"/>
      <polygon points="135,600 600,700 1065,600 1065,615 600,724 135,615" fill="var(--orange)"/>
    </svg>
    <h1 class="abs hero-title" style="left:552px;top:240px">Law Enforcement<br>Security Consulting</h1>
    <p class="abs hero-sub" style="left:554px;top:378px">Services on an incident-based or retainer basis</p>
    <div class="btn" style="left:560px;top:443px;width:176px;height:40px">Get Started</div>
    <div class="dots" style="left:574px;top:647px"><i></i><i class="on"></i><i></i></div>
  </section>

  <!-- Trusted resource -->
  <section>
    <svg class="layer" width="1200" height="1300" viewBox="0 0 1200 1300">
      <defs>
        <linearGradient id="aboutGrad" x1="0" y1="0" x2="1" y2="1">
          <stop offset="0" stop-color="#2a2d36"/>
          <stop offset="1" stop-color="#8a7466"/>
        </linearGradient>
      </defs>
      <polygon points="255,788 145,850 145,985 165,985 165,862 255,810" fill="var(--orange)"/>
      <polygon points="370,788 475,850 475,985 455,985 455,862 370,810" fill="var(--orange)"/>
      <polygon role="img" aria-label="Agency officer photo within a hexagon frame" points="310,830 440,905 440,1075 310,1150 180,1075 180,905" fill="url(#aboutGrad)"/>
      <polygon points="180,1110 310,1188 440,1110 450,1128 310,1208 170,1128" fill="var(--orange)"/>
    </svg>
    <h2 class="abs heading" style="left:610px;top:808px;font-weight:800;font-size:34px;line-height:50px">A Trusted Resource<br><span style="font-weight:400">for Law Enforcement</span></h2>
    <p class="abs para" style="left:610px;top:945px;width:445px">Sed ut perspiciatis unde omnis iste natus error sit voluptatem accusantium doloremque laudantium, totam rem aperiam, eaque ipsa quae ab illo inventore veritatis et quasi architecto beatae vitae dicta sunt explicabo. Nemo enim ipsam voluptatem quia voluptas sit aspernatur aut odit aut fugit, sed quia consequuntur magni dolores eos qui ratione voluptatem sequi nesciunt.</p>
    <div class="btn" style="left:610px;top:1133px;width:160px;height:40px">Read More</div>
  </section>

  <!-- Services -->
  <section>
    <svg class="layer" width="1200" height="2300" viewBox="0 0 1200 2300">
      <polygon points="0,1400 600,1290 1200,1400 1200,2110 600,2270 0,2110" fill="var(--light)"/>
      <polygon points="135,1392 600,1266 1065,1392 1065,1406 600,1290 135,1406" fill="var(--orange)"/>
      <polygon points="0,2104 600,2262 1200,2104 1200,2118 600,2284 0,2118" fill="var(--orange)"/>
    </svg>
    <h2 class="abs heading center" style="top:1415px"><b>Our</b> Services</h2>
    <span class="rule" style="left:578px;top:1470px"></span>

    <div class="card" style="left:145px;top:1518px">
      <svg width="296" height="336"><polygon points="148,1 295,74 295,262 148,335 1,262 1,74" fill="#fff" stroke="var(--orange)" stroke-width="1.5"/></svg>
      <span class="icon" role="img" aria-label="Fire extinguisher icon"></span>
      <h3>Fire &amp; EMS</h3>
      <p>Sed ut perspiciatis unde omnis iste natus error sit voluptatem accusantium doloremque laudantium, totam rem aperiam, eaque ipsa quae ab illo</p>
      <svg class="go" viewBox="0 0 22 22"><circle cx="11" cy="11" r="9.5" fill="none" stroke="#333" stroke-width="1.4"/><path d="M11 6v9M7 11l4 4 4-4" fill="none" stroke="#333" stroke-width="1.4"/></svg>
    </div>
    <div class="card featured" style="left:452px;top:1518px">
      <svg width="296" height="336"><polygon points="148,1 295,74 295,262 148,335 1,262 1,74" fill="var(--orange)"/></svg>
      <span class="icon" role="img" aria-label="Police officer icon"></span>
      <h3>Police Services</h3>
      <p>Sed ut perspiciatis unde omnis iste natus error sit voluptatem accusantium doloremque laudantium, totam rem aperiam, eaque ipsa quae ab illo</p>
      <svg class="go" viewBox="0 0 22 22"><circle cx="11" cy="11" r="9.5" fill="none" stroke="#fff" stroke-width="1.4"/><path d="M11 6v9M7 11l4 4 4-4" fill="none" stroke="#fff" stroke-width="1.4"/></svg>
    </div>
    <div class="card" style="left:759px;top:1518px">
      <svg width="296" height="336"><polygon points="148,1 295,74 295,262 148,335 1,262 1,74" fill="#fff" stroke="var(--orange)" stroke-width="1.5"/></svg>
      <span class="icon" role="img" aria-label="Community network icon"></span>
      <h3>Community Development</h3>
      <p>Sed ut perspiciatis unde omnis iste natus error sit voluptatem accusantium doloremque laudantium, totam rem aperiam, eaque ipsa quae ab illo</p>
      <svg class="go" viewBox="0 0 22 22"><circle cx="11" cy="11" r="9.5" fill="none" stroke="#333" stroke-width="1.4"/><path d="M11 6v9M7 11l4 4 4-4" fill="none" stroke="#333" stroke-width="1.4"/></svg>
    </div>
    <div class="card" style="left:299px;top:1790px">
      <svg width="296" height="336"><polygon points="148,1 295,74 295,262 148,335 1,262 1,74" fill="#fff" stroke="var(--orange)" stroke-width="1.5"/></svg>
      <span class="icon" role="img" aria-label="Clerk at desk icon"></span>
      <h3>Clerk's Office</h3>
      <p>Sed ut perspiciatis unde omnis iste natus error sit voluptatem accusantium doloremque laudantium, totam rem aperiam, eaque ipsa quae ab illo</p>
      <svg class="go" viewBox="0 0 22 22"><circle cx="11" cy="11" r="9.5" fill="none" stroke="#333" stroke-width="1.4"/><path d="M11 6v9M7 11l4 4 4-4" fill="none" stroke="#333" stroke-width="1.4"/></svg>
    </div>
    <div class="card" style="left:605px;top:1790px">
      <svg width="296" height="336"><polygon points="148,1 295,74 295,262 148,335 1,262 1,74" fill="#fff" stroke="var(--orange)" stroke-width="1.5"/></svg>
      <span class="icon" role="img" aria-label="Economic growth icon"></span>
      <h3>Economic Development</h3>
      <p>Sed ut perspiciatis unde omnis iste natus error sit voluptatem accusantium doloremque laudantium, totam rem aperiam, eaque ipsa quae ab illo</p>
      <svg class="go" viewBox="0 0 22 22"><circle cx="11" cy="11" r="9.5" fill="none" stroke="#333" stroke-width="1.4"/><path d="M11 6v9M7 11l4 4 4-4" fill="none" stroke="#333" stroke-width="1.4"/></svg>
    </div>
  </section>

  <!-- How it works -->
  <section>
    <svg class="layer" width="1200" height="2800" viewBox="0 0 1200 2800">
      <defs>
        <linearGradient id="howGrad" x1="0" y1="0" x2="1" y2="1">
          <stop offset="0" stop-color="#d9d6d2"/>
          <stop offset="1" stop-color="#8f8a86"/>
        </linearGradient>
      </defs>
      <polygon points="745,2375 845,2430 845,2640 745,2695 645,2640 645,2430" fill="var(--orange)"/>
      <polygon points="890,2395 1090,2510 1090,2690 890,2720 770,2665" fill="none" stroke="var(--orange)" stroke-width="2"/>
      <polygon role="img" aria-label="Smiling consultant working at a laptop" points="885,2355 1055,2450 1055,2645 885,2740 715,2645 715,2450" fill="url(#howGrad)"/>
    </svg>
    <h2 class="abs heading" style="left:143px;top:2385px"><b>How It</b> Works</h2>
    <p class="abs para" style="left:143px;top:2473px;width:447px">Sed ut perspiciatis unde omnis iste natus error sit voluptatem accusantium doloremque laudantium, totam rem aperiam, eaque ipsa quae ab illo inventore veritatis et quasi architecto beatae vitae dicta sunt explicabo. Nemo enim ipsam voluptatem quia voluptas sit aspernatur aut odit aut fugit, sed quia consequuntur magni dolores eos qui ratione voluptatem sequi nesciunt.</p>
    <div class="btn" style="left:143px;top:2670px;width:163px;height:40px">Read More</div>
  </section>

  <!-- Team -->
  <section>
    <svg class="layer" width="1200" height="3620" viewBox="0 0 1200 3620">
      <defs>
        <linearGradient id="teamGrad" x1="0" y1="0" x2="1" y2="1">
          <stop offset="0" stop-color="#2a130b"/>
          <stop offset=".55" stop-color="#1c1a1c"/>
          <stop offset="1" stop-color="#2f4653"/>
        </linearGradient>
        <linearGradient id="personGrad" x1="0" y1="0" x2="0" y2="1">
          <stop offset="0" stop-color="#d8d4d0"/>
          <stop offset="1" stop-color="#2d3547"/>
        </linearGradient>
      </defs>
      <polygon role="img" aria-label="Dark city skyline backdrop" points="0,2925 600,2810 1200,2925 1200,3490 600,3600 0,3490" fill="url(#teamGrad)"/>
      <polygon points="135,2905 600,2783 1065,2905 1065,2920 600,2805 135,2920" fill="var(--orange)"/>
      <polygon points="183,3050 294,3113 294,3252 183,3315 72,3252 72,3113" fill="none" stroke="#5a2b1a" stroke-width="6"/>
      <polygon points="460,3133 571,3196 571,3335 460,3398 349,3335 349,3196" fill="none" stroke="var(--orange)" stroke-width="6"/>
      <polygon points="740,3050 851,3113 851,3252 740,3315 629,3252 629,3113" fill="none" stroke="#5a2b1a" stroke-width="6"/>
      <polygon points="1018,3133 1129,3196 1129,3335 1018,3398 907,3335 907,3196" fill="none" stroke="#5a2b1a" stroke-width="6"/>
    </svg>
    <h2 class="abs heading center" style="top:2945px;color:#fff"><b>Meet</b> Our Team</h2>
    <span class="rule" style="left:578px;top:3000px"></span>
    <div class="member" style="left:53px;top:3062px"><div class="photo" role="img" aria-label="Portrait of team member John Doe" style="background:linear-gradient(#e4e1dd,#2f3748);height:242px;width:196px"></div><div class="name">John Doe</div><div class="role">Lorem upsum dolor</div></div>
    <div class="member" style="left:330px;top:3145px"><div class="photo" role="img" aria-label="Portrait of team member Smith John" style="background:linear-gradient(#e4e1dd,#2f3748);height:242px;width:196px"></div><div class="name">Smith John</div><div class="role">Lorem upsum dolor</div></div>
    <div class="member" style="left:610px;top:3062px"><div class="photo" role="img" aria-label="Portrait of team member Deo Leos" style="background:linear-gradient(#e4e1dd,#2f3748);height:242px;width:196px"></div><div class="name">Deo Leos</div><div class="role">Lorem upsum dolor</div></div>
    <div class="member" style="left:888px;top:3145px"><div class="photo" role="img" aria-label="Portrait of team member Andrews Sam" style="background:linear-gradient(#e4e1dd,#2f3748);height:242px;width:196px"></div><div class="name">Andrews Sam</div><div class="role">Lorem upsum dolor</div></div>
    <div class="dots" style="left:572px;top:3528px"><i></i><i class="on"></i><i></i></div>
  </section>

  <!-- Why work with us -->
  <section>
    <svg class="layer" width="1200" height="4400" viewBox="0 0 1200 4400">
      <defs>
        <linearGradient id="whyGrad" x1="0" y1="0" x2="1" y2="1">
          <stop offset="0" stop-color="#e9e6e2"/>
          <stop offset="1" stop-color="#2c3854"/>
        </linearGradient>
      </defs>
      <polygon points="470,3875 620,3960 620,4140 470,4225 320,4140 320,3960" fill="var(--orange)"/>
      <polygon points="90,4040 270,3940 270,4335 90,4230" fill="none" stroke="var(--orange)" stroke-width="2"/>
      <polygon role="img" aria-label="Confident consultant with crossed arms" points="330,3885 510,3990 510,4275 330,4380 150,4275 150,3990" fill="url(#whyGrad)"/>
    </svg>
    <h2 class="abs heading center" style="top:3757px"><b>Why Work</b> With Us?</h2>
    <span class="rule" style="left:578px;top:3812px"></span>
    <div class="abs reason" style="left:725px;top:3908px;width:300px">
      <h4>Proven Techniques</h4>
      <p>Sed ut perspiciatis unde omnis iste natus error sit voluptatem accusantium doloremque laudantium rem aeaque ipsa quae ab illo</p>
      <svg width="26" height="26" viewBox="0 0 26 26"><circle cx="13" cy="13" r="11.5" fill="none" stroke="var(--orange)" stroke-width="1.6"/><path d="M7 13h11M14 9l4 4-4 4" fill="none" stroke="#333" stroke-width="1.6"/></svg>
    </div>
    <div class="abs reason" style="left:725px;top:4060px;width:300px">
      <h4>Flexibility &amp; Scalability</h4>
      <p>Sed ut perspiciatis unde omnis iste natus error sit voluptatem accusantium doloremque laudantium rem aeaque ipsa quae ab illo</p>
      <svg width="26" height="26" viewBox="0 0 26 26"><circle cx="13" cy="13" r="11.5" fill="none" stroke="var(--orange)" stroke-width="1.6"/><path d="M7 13h11M14 9l4 4-4 4" fill="none" stroke="#333" stroke-width="1.6"/></svg>
    </div>
    <div class="abs reason" style="left:725px;top:4212px;width:300px">
      <h4>Experience</h4>
      <p>Sed ut perspiciatis unde omnis iste natus error sit voluptatem accusantium doloremque laudantium rem aeaque ipsa quae ab illo</p>
      <svg width="26" height="26" viewBox="0 0 26 26"><circle cx="13" cy="13" r="11.5" fill="none" stroke="var(--orange)" stroke-width="1.6"/><path d="M7 13h11M14 9l4 4-4 4" fill="none" stroke="#333" stroke-width="1.6"/></svg>
    </div>
  </section>

  <!-- Contact -->
  <section>
    <svg class="layer" width="1200" height="5220" viewBox="0 0 1200 5220">
      <defs>
        <linearGradient id="contactGrad" x1="0" y1="0" x2="1" y2="1">
          <stop offset="0" stop-color="#8a8f99"/>
          <stop offset="1" stop-color="#2b3a63"/>
        </linearGradient>
      </defs>
      <polygon points="0,4535 600,4392 1200,4535 1200,5070 600,5180 0,5070" fill="var(--slate)"/>
      <polygon role="img" aria-label="Smiling senior consultant in a navy suit" points="640,4470 1200,4535 1200,5070 600,5180" fill="url(#contactGrad)"/>
      <polygon points="0,4535 540,4408 660,4470 600,5180 0,5070" fill="var(--orange)"/>
      <polygon points="135,4528 600,4388 1065,4528 1065,4543 600,4410 135,4543" fill="var(--orange)"/>
      <polygon points="0,5068 600,5180 1200,5068 1200,5082 600,5196 0,5082" fill="var(--orange)"/>
    </svg>
    <h2 class="abs heading" style="left:145px;top:4595px;color:#fff"><b>Contact</b> Us</h2>
    <span class="rule" style="left:145px;top:4652px;background:#fff"></span>
    <div class="field" style="left:145px;top:4700px;width:190px;height:40px">Enter Name</div>
    <div class="field" style="left:345px;top:4700px;width:190px;height:40px">Enter Email</div>
    <div class="field" style="left:145px;top:4752px;width:190px;height:40px">Enter Phone</div>
    <div class="field" style="left:345px;top:4752px;width:190px;height:40px">Enter Address</div>
    <div class="field" style="left:145px;top:4805px;width:390px;height:105px">Message</div>
    <div class="btn" style="left:150px;top:4930px;width:155px;height:40px;background:var(--ink)">Submit</div>
  </section>

  <!-- Footer -->
  <footer>
    <div class="abs brand" style="left:145px;top:5230px">
      <span class="mark" style="width:70px;height:70px"></span>
      <span class="name" style="font-size:32px">Brennock Group</span>
    </div>
    <nav class="abs foot-nav" style="left:573px;top:5234px">
      <span style="width:82px">Home</span>
      <span style="width:113px">Services</span>
      <span style="width:115px">About Us</span>
      <span style="width:100px">Clients</span>
      <span>Contact</span>
    </nav>
    <p class="abs copy" style="left:573px;top:5276px">© 2025 Brennock Group.All Rights Reserved &nbsp;|&nbsp; Privacy Policy &nbsp;|&nbsp; Terms of use</p>
    <div class="abs social" style="left:573px;top:5306px"><i></i><i style="border-color:var(--orange)"></i><i></i></div>
  </footer>

</div>
</body>
</html>
```